Ice Cream Container Print Design

This is an ice cream cup. This is for a homemade raspberry ice cream. I need it to be eye catching, pops from the shelf, with a gourmet look as well. I am looking for more of the Vollmer Strint Ice cream type of style with it being elegant but also fun.

This goes into grocery shelves in the freezer. It has a clear lid so that is not included. The design sheet is for the space that wraps around the cup.

Target Market(s)

Grocery freezer shelves

Industry/Entity Type

Food Production

Font styles to use
Serif
Script

Colors
ec1f27
ffc214

Requirements
Must have
• Orvin's Logo and Fox Hollow. Please also use the berry cluster. I would like reds, golds, and blacks. I want a background design or color.
• I want it to say "Homemade Raspberry Ice Cream"
Nice to have
• As the spec sheet indicates on the bottom left, please make the front repeat 2 times as is goes around the cup.
Should not have
• Please do not make it look like a clown show. I want it fun and gourmet looking.

```html
<!DOCTYPE html>
<html lang="en">
<head>
<meta charset="utf-8">
<title>Orvin's Fox Hollow – Homemade Raspberry Ice Cream Wrap</title>
<link rel="stylesheet" href="https://fonts.googleapis.com/css2?family=Libre+Baskerville:wght@400;700&display=swap">
<style>
  :root {
    --stage: #e6e6e8;
    --paper: #ffffff;
    --cream: #fde6b0;
    --berry-red: #ec1f27;
    --berry-deep: #c9141b;
    --gold: #c2901a;
  }
  * { margin: 0; padding: 0; box-sizing: border-box; }
  html, body {
    width: 1200px;
    height: 722px;
    overflow: hidden;
    background: var(--stage);
  }
  .wrap-sheet {
    position: absolute;
    left: 20px;
    top: 192px;
    width: 1160px;
    height: 337px;
    background: linear-gradient(to bottom,
      var(--paper) 0,
      var(--paper) 158px,
      var(--cream) 322px);
    display: flex;
    overflow: hidden;
  }
  .wrap-sheet::after {
    content: "";
    position: absolute;
    left: 0; right: 0; bottom: 0;
    height: 15px;
    background: var(--berry-red);
  }
  .front-panel {
    position: relative;
    flex: 1 1 0;
    height: 100%;
  }
  .brand {
    position: absolute;
    left: 0; right: 0;
    top: 62px;
    text-align: center;
    font-family: "Libre Baskerville", serif;
    font-weight: 700;
    color: var(--gold);
    line-height: 1.12;
  }
  .brand-owner { display: block; font-size: 38px; }
  .brand-place { display: block; font-size: 38px; }
  .flavor-row {
    position: absolute;
    left: 0; right: 0;
    top: 182px;
    height: 112px;
  }
  .berry-art {
    position: absolute;
    top: 0;
    width: 92px;
    height: 111px;
    border-radius: 46% 46% 50% 50% / 40% 40% 60% 60%;
    background: radial-gradient(circle at 45% 40%, var(--berry-red), var(--berry-deep));
  }
  .berry-art.left { left: 39px; }
  .berry-art.right { left: 255px; }
  .flavor-name {
    position: absolute;
    left: 131px;
    width: 124px;
    top: 26px;
    text-align: center;
    font-family: "Libre Baskerville", serif;
    font-size: 17px;
    line-height: 21px;
    color: var(--berry-red);
  }
  .flavor-name span { display: block; }
</style>
</head>
<body>
  <main class="wrap-sheet">
    <section class="front-panel">
      <h1 class="brand"><span class="brand-owner">Orvin's</span><span class="brand-place">Fox Hollow</span></h1>
      <div class="flavor-row">
        <div class="berry-art left" role="img" aria-label="Red outlined raspberry illustration"></div>
        <p class="flavor-name"><span>Homemade</span><span>Raspberry</span><span>Ice Cream</span></p>
        <div class="berry-art right" role="img" aria-label="Red outlined raspberry illustration"></div>
      </div>
    </section>
    <section class="front-panel">
      <h1 class="brand"><span class="brand-owner">Orvin's</span><span class="brand-place">Fox Hollow</span></h1>
      <div class="flavor-row">
        <div class="berry-art left" role="img" aria-label="Red outlined raspberry illustration"></div>
        <p class="flavor-name"><span>Homemade</span><span>Raspberry</span><span>Ice Cream</span></p>
        <div class="berry-art right" role="img" aria-label="Red outlined raspberry illustration"></div>
      </div>
    </section>
    <section class="front-panel">
      <h1 class="brand"><span class="brand-owner">Orvin's</span><span class="brand-place">Fox Hollow</span></h1>
      <div class="flavor-row">
        <div class="berry-art left" role="img" aria-label="Red outlined raspberry illustration"></div>
        <p class="flavor-name"><span>Homemade</span><span>Raspberry</span><span>Ice Cream</span></p>
        <div class="berry-art right" role="img" aria-label="Red outlined raspberry illustration"></div>
      </div>
    </section>
  </main>
</body>
</html>
```